2 guided dives on the North of Bonaire

2 guided shore dives on the North of Bonaire including authentic local lunch and drinks.
We offer an adventure for experienced divers to discover the dive sites on the north of the island.
Showing you the beauty of the reefs and tasting authentic local cuisine like goat or iguana combined with a stunning view of the surroundings.

Target Market(s)

Divers / tourism

Industry/Entity Type

Tourism / Diving

Font styles to use
Sans Serif

Colors
0054AA
0677BA
7BADD7
CADEEF
E8F1F8
0094D4
00A9DD
6FCCEA
C7EBF8
E9F6FB
F0912C
F2A743
F7CA91
FBE8D2
FDF5EE
EE7325
F08F49
F5BC92
FAE3D3
FDF4ED

Requirements
Must have
• Some of the pictures I uploaded and the food picture / bottom like in the pictures
Nice to have
• inviting to join us on the guided dives
Should not have
• Any picture I didn't provide

```html
<!DOCTYPE html>
<html lang="en">
<head>
<meta charset="utf-8">
<title>Reef Roam – Guided Dives Flyer</title>
<link href="https://fonts.googleapis.com/css2?family=Poppins:wght@400;500;600;700;800;900&display=swap" rel="stylesheet">
<style>
  :root {
    --navy: #1d2f52;
    --navy-deep: #15223d;
    --blue-deep: #0054AA;
    --blue: #0677BA;
    --sky: #7BADD7;
    --sky-soft: #a8d1f0;
    --sky-pale: #CADEEF;
    --cyan: #00A9DD;
    --orange: #F0912C;
    --orange-warm: #F2A743;
    --orange-soft: #F7CA91;
    --white: #ffffff;
  }
  * { margin: 0; padding: 0; box-sizing: border-box; }
  html, body { width: 882px; height: 1200px; overflow: hidden; }
  body { font-family: "Poppins", sans-serif; background: var(--sky-soft); }

  .flyer { position: relative; width: 882px; height: 1200px; overflow: hidden; background: var(--sky-soft); }
  .backdrop { position: absolute; inset: 0; }

  .photo-circle {
    position: absolute; border-radius: 50%;
    border: 10px solid var(--orange);
  }
  .photo-seahorse {
    left: 640px; top: -20px; width: 262px; height: 262px;
    background: radial-gradient(circle at 55% 50%, #b46a3a 0%, #4e6f78 35%, #203f55 75%);
  }
  .photo-food {
    left: 560px; top: 250px; width: 170px; height: 170px;
    background: radial-gradient(circle at 50% 50%, #e6a64c 0%, #c4792e 45%, #7a4a22 85%);
  }

  .headline {
    position: absolute; left: 0; right: 0; top: 420px;
    text-align: center; font-weight: 800; line-height: 1;
  }
  .headline .line-top { display: block; color: var(--orange); font-size: 122px; letter-spacing: -2px; }
  .headline .line-bottom { display: block; color: var(--navy); font-size: 130px; letter-spacing: -3px; margin-top: 4px; }

  .steps { position: absolute; top: 745px; left: 98px; right: 82px; display: flex; gap: 40px; }
  .step { flex: 1; position: relative; padding-top: 46px; }
  .step-icon {
    position: absolute; top: 0; left: 50%; transform: translateX(-50%);
    width: 56px; height: 56px; border-radius: 50%; background: var(--navy);
    display: flex; align-items: center; justify-content: center;
  }
  .step-number {
    position: absolute; top: 14px; left: calc(50% + 34px);
    width: 32px; height: 32px; border-radius: 50%;
    background: var(--white); border: 3px solid var(--navy);
    color: var(--navy); font-weight: 700; font-size: 17px;
    display: flex; align-items: center; justify-content: center;
  }
  .step-card {
    background: var(--white); border: 5px solid var(--orange); border-radius: 14px;
    height: 136px; padding: 26px 22px; display: flex; align-items: center;
    color: var(--navy); font-size: 25px; font-weight: 500; line-height: 1.25;
  }

  .cta {
    position: absolute; top: 935px; left: 50%; transform: translateX(-50%);
    background: var(--orange); color: var(--navy); font-weight: 800; font-size: 40px;
    padding: 8px 42px; border-radius: 40px; letter-spacing: 0.5px;
  }

  .footer { position: absolute; left: 0; right: 0; bottom: 0; height: 160px; }
  .brand {
    position: absolute; left: 22px; top: 4px; width: 136px; height: 136px; border-radius: 50%;
    background: var(--navy); border: 4px solid var(--white);
    display: flex; align-items: center; justify-content: center;
    color: var(--white); font-weight: 700; font-size: 24px; text-align: center; line-height: 1.05;
  }
  .highlights { position: absolute; left: 248px; top: 22px; display: flex; gap: 28px; }
  .highlight {
    display: flex; gap: 10px; width: 290px;
    color: var(--white); font-size: 15px; line-height: 1.3;
  }
  .highlight::before {
    content: ""; flex: none; width: 14px; height: 14px; margin-top: 3px;
    border-radius: 50%; background: var(--orange-warm);
  }
  .contact { position: absolute; left: 196px; top: 94px; display: flex; gap: 40px; }
  .contact-pill {
    display: flex; align-items: center; gap: 10px; height: 42px; padding: 0 20px 0 16px;
    border-radius: 22px; font-weight: 700; font-size: 19px;
  }
  .contact-phone { background: var(--orange-warm); color: var(--navy); }
  .contact-web { background: var(--blue); color: var(--white); }
  .contact-icon {
    width: 28px; height: 28px; border-radius: 50%;
    display: flex; align-items: center; justify-content: center;
  }
  .contact-phone .contact-icon { background: var(--navy); }
  .contact-web .contact-icon { background: var(--white); }
</style>
</head>
<body>
<main class="flyer">
  <svg class="backdrop" width="882" height="1200" viewBox="0 0 882 1200">
    <defs>
      <linearGradient id="coast" x1="0" y1="0" x2="0" y2="1">
        <stop offset="0" stop-color="#4d8fd6"/>
        <stop offset="0.35" stop-color="#a9cdea"/>
        <stop offset="0.5" stop-color="#2e86b8"/>
        <stop offset="0.7" stop-color="#6c7c86"/>
        <stop offset="1" stop-color="#a29a8c"/>
      </linearGradient>
    </defs>
    <!-- soft waves -->
    <path d="M0 540 C 200 470, 420 600, 882 500 L 882 1200 L 0 1200 Z" fill="#b7dbf4"/>
    <path d="M0 980 C 260 940, 520 1060, 882 970 L 882 1200 L 0 1200 Z" fill="#c6e4f8"/>
    <!-- coastal photo area -->
    <path d="M0 0 H 882 V 90 C 760 300, 560 430, 330 430 C 180 430, 70 390, 0 350 Z"
          fill="var(--orange)"/>
    <path d="M0 0 H 870 V 80 C 750 285, 555 412, 330 412 C 185 412, 75 375, 0 336 Z"
          fill="url(#coast)" role="img" aria-label="Photo of a rocky coral shoreline with turquoise sea and blue sky"/>
    <!-- footer band -->
    <path d="M0 1052 C 300 1030, 600 1070, 882 1040 L 882 1200 L 0 1200 Z" fill="var(--sky)"/>
    <path d="M0 1066 C 300 1046, 600 1082, 882 1054 L 882 1200 L 0 1200 Z" fill="var(--navy)"/>
  </svg>

  <div class="photo-circle photo-seahorse" role="img" aria-label="Underwater photo of a seahorse"></div>
  <div class="photo-circle photo-food" role="img" aria-label="Photo of authentic local food"></div>

  <h1 class="headline">
    <span class="line-top">Let Us</span>
    <span class="line-bottom">Guide You!</span>
  </h1>

  <section class="steps">
    <div class="step">
      <div class="step-icon">
        <svg width="34" height="34" viewBox="0 0 34 34" fill="none" stroke="#fff" stroke-width="2.6" stroke-linecap="round">
          <circle cx="22" cy="9" r="4" fill="#fff" stroke="none"/>
          <path d="M6 20 L 20 15 L 26 19"/>
          <path d="M4 27 C 10 23, 14 31, 20 27 S 28 25, 30 27"/>
        </svg>
      </div>
      <div class="step-number">1</div>
      <div class="step-card">We show you the cool stuff</div>
    </div>
    <div class="step">
      <div class="step-icon">
        <svg width="34" height="34" viewBox="0 0 34 34" fill="none" stroke="#fff" stroke-width="2.6" stroke-linecap="round">
          <circle cx="8" cy="12" r="4" fill="#fff" stroke="none"/>
          <path d="M12 16 L 26 20 L 31 16"/>
          <path d="M14 22 L 22 26"/>
        </svg>
      </div>
      <div class="step-number">2</div>
      <div class="step-card">You just enjoy the dives, we take care of the rest</div>
    </div>
  </section>

  <div class="cta">JOIN US NOW!</div>

  <footer class="footer">
    <div class="brand">Reef<br>Roam</div>
    <div class="highlights">
      <p class="highlight">Two guided dives at Klein Bonaire / North Coast</p>
      <p class="highlight">Lunch, fruit, premium open bar and deluxe BBQ-diner is included</p>
    </div>
    <div class="contact">
      <div class="contact-pill contact-phone">
        <span>Call us</span>
        <span class="contact-icon">
          <svg width="16" height="16" viewBox="0 0 24 24" fill="#fff"><path d="M6.6 10.8a15 15 0 0 0 6.6 6.6l2.2-2.2a1 1 0 0 1 1-.25 11.4 11.4 0 0 0 3.6.57 1 1 0 0 1 1 1V20a1 1 0 0 1-1 1A17 17 0 0 1 3 4a1 1 0 0 1 1-1h3.5a1 1 0 0 1 1 1c0 1.25.2 2.46.57 3.6a1 1 0 0 1-.25 1z"/></svg>
        </span>
        <span>+(599) 555 01 42</span>
      </div>
      <div class="contact-pill contact-web">
        <span class="contact-icon">
          <svg width="18" height="18" viewBox="0 0 24 24" fill="none" stroke="#0677BA" stroke-width="2"><circle cx="12" cy="12" r="9"/><path d="M3 12h18M12 3c3 3 3 15 0 18M12 3c-3 3-3 15 0 18"/></svg>
        </span>
        <span>www.reefroam-dive.com</span>
      </div>
    </div>
  </footer>
</main>
</body>
</html>
```